Tabloid Magazine Flyer Class Action Lawsuit

Create a bold, 2-page 8.5" x 11" flyer with the look and feel of a tabloid exposé — loud, sensational, and impossible to ignore. Use bold fonts, dramatic headlines, and high-contrast colors (red, black, white, deep blue). Fill every inch of space — no white space, no subtlety. Use the provided images prominently. Page 1 should grab attention with a shocking headline, impactful image, and strong call to action. Page 2 should stack bold subheadings and explosive bullet points. Emphasize urgency, outrage, and grassroots power. This flyer is meant to rally a community.
Updates

Need to extend because we haven't received a design that meets our needs

Target Market(s)

All instructions and content are in the attached word doc

Industry/Entity Type

Requirements
Must have
• All instructions and content are in the attached word doc
Nice to have
Should not have

```html
<!DOCTYPE html>
<html lang="en">
<head>
<meta charset="utf-8">
<title>Save Seabright Park – Community Flyer</title>
<link rel="stylesheet" href="https://fonts.googleapis.com/css2?family=Montserrat:wght@400;500;600;700;800&display=swap">
<style>
  :root {
    --backdrop: #cfcfcf;
    --red: #cf3a2c;
    --red-deep: #b92d22;
    --blue: #1b5a9a;
    --navy: #0f1a3f;
    --ink: #101a33;
    --white: #ffffff;
  }
  * { box-sizing: border-box; margin: 0; padding: 0; }
  html, body { width: 1200px; height: 2258px; overflow: hidden; }
  body { background: var(--backdrop); font-family: 'Montserrat', Arial, sans-serif; position: relative; }

  .page { position: absolute; left: 196px; width: 808px; height: 1045px; overflow: hidden; }
  .page-front { top: 78px; background: var(--white); }
  .page-back { top: 1152px; background: var(--navy); color: var(--white); }

  .brand-box {
    position: absolute; background: var(--white);
    display: flex; align-items: center; justify-content: center;
  }
  .brand-name { font-weight: 800; color: var(--ink); font-size: 34px; line-height: 1.1; letter-spacing: 1px; text-align: center; }

  /* front */
  .front-hero {
    position: absolute; left: 0; top: 0; width: 808px; height: 564px;
    background: linear-gradient(100deg, var(--red) 0%, var(--red-deep) 45%, var(--red) 100%);
    color: var(--white); text-align: center;
  }
  .front-hero .brand-box { left: 260px; top: 0; width: 288px; height: 181px; }
  .hero-headline { position: absolute; top: 218px; width: 100%; font-weight: 800; font-size: 31px; line-height: 39px; letter-spacing: .5px; }
  .hero-rally { position: absolute; top: 372px; width: 100%; font-weight: 700; font-size: 22px; letter-spacing: .5px; }
  .hero-fact { position: absolute; top: 421px; width: 100%; font-weight: 700; font-size: 14px; line-height: 19px; }
  .hero-invite { position: absolute; top: 478px; width: 100%; font-weight: 700; font-size: 20px; }
  .hero-meeting { position: absolute; top: 508px; width: 100%; font-weight: 800; font-size: 25px; letter-spacing: .5px; }

  .event-band {
    position: absolute; left: 0; top: 564px; width: 808px; height: 79px;
    background: var(--blue); color: var(--white); text-align: center;
  }
  .event-date { font-weight: 800; font-size: 31px; padding-top: 8px; line-height: 36px; }
  .event-place { font-weight: 700; font-size: 17px; }

  .front-call { position: absolute; top: 643px; left: 0; width: 808px; height: 402px; color: var(--ink); text-align: center; }
  .call-headline { margin-top: 32px; font-weight: 800; font-size: 29px; line-height: 37px; letter-spacing: .5px; }
  .lawsuit-title { margin-top: 38px; font-weight: 700; font-size: 14px; }
  .lawsuit-copy { font-size: 15px; line-height: 19px; }
  .site-link { margin-top: 38px; font-weight: 800; font-size: 27px; color: var(--blue); }

  /* back */
  .page-back .brand-box { left: 495px; top: 0; width: 285px; height: 180px; }
  .exposed-intro { position: absolute; left: 51px; top: 44px; width: 430px; font-size: 12.5px; line-height: 16px; }
  .exposed-intro strong { font-weight: 700; }
  .facts-title { position: absolute; left: 51px; top: 164px; font-weight: 800; font-size: 18px; letter-spacing: .3px; }
  .facts { position: absolute; left: 51px; top: 199px; width: 706px; }
  .fact { margin-bottom: 16px; }
  .fact-title { font-weight: 700; font-size: 12.5px; line-height: 16px; text-transform: uppercase; }
  .fact-copy { font-size: 12.5px; line-height: 16px; }

  .park-photo {
    position: absolute; left: 0; bottom: 0; width: 808px; height: 246px;
    background: linear-gradient(180deg, #1d2a55 0%, #5a3a4a 40%, #b26a3e 65%, #3a3040 100%);
  }
  .park-photo .site-link { position: absolute; left: 0; width: 100%; top: 172px; margin: 0; text-align: center; color: var(--white); font-size: 29px; }
  .back-rally { position: absolute; z-index: 2; left: 0; top: 776px; width: 808px; text-align: center; font-weight: 800; font-size: 21px; line-height: 27px; letter-spacing: .3px; }
</style>
</head>
<body>

<section class="page page-front">
  <div class="front-hero">
    <div class="brand-box"><span class="brand-name">ACCESS<br>FOR ALL</span></div>
    <h1 class="hero-headline">SEABRIGHT PARK EXPOSED<br>DISABLED CHILD TRAUMATIZED<br>PUBLIC LAND ABUSED FOR PROFIT</h1>
    <p class="hero-rally">HELP OUR BEACH COMMUNITY FIGHT BACK</p>
    <p class="hero-fact">SEABRIGHT PARK IS NOT PRIVATE. IT IS PUBLIC PROPERTY<br>OWNED BY THE CITY, PAID FOR BY YOU.</p>
    <p class="hero-invite">JOIN us &amp; SHOW YOUR SUPPORT @</p>
    <p class="hero-meeting">CORAL BEACH TOWN COUNCIL MEETING</p>
  </div>
  <div class="event-band">
    <p class="event-date">Date: May 14, 2025 – 6:00 PM</p>
    <p class="event-place">Place: Seabright Park Community Room (Above the Arcade)</p>
  </div>
  <div class="front-call">
    <h2 class="call-headline">HELP OUR COMMUNITY SAVE<br>SEABRIGHT PARK<br>SEABRIGHT PARK WAS BUILT FOR<br>FAMILIES — NOT RAVES</h2>
    <p class="lawsuit-title">CLASS ACTION LAWSUIT FORMING NOW!</p>
    <p class="lawsuit-copy">If you’ve been impacted by noise, denied public access, or harmed by these violations,<br>you may be eligible for compensation.<br>We’re gathering stories and preparing legal action.</p>
    <p class="site-link">www.FixSeabrightPark.com</p>
  </div>
</section>

<section class="page page-back">
  <div class="brand-box"><span class="brand-name">ACCESS<br>FOR ALL</span></div>
  <p class="exposed-intro"><strong>EXPOSED: Marco Vellan,</strong> CEO of Harbor Asset Pool XII LLC the leaseholder of Seabright Park, has drawn community outrage for profiting off public land while operating Seabright Park in ways many say violate its lease and damage our beach, our peace, and our environment — all from his luxury estate in Rancho Verde.</p>
  <h2 class="facts-title">WHAT THEY DON’T WANT YOU TO KNOW:</h2>
  <div class="facts">
    <div class="fact"><p class="fact-title">Illegal raves – no permits.</p><p class="fact-copy">Explosive concerts over 100 decibels, blasting Coral Beach with bass — multiple times per week. According to Public Records these events had NO PERMITS &amp; NO CITY APPROVAL.</p></div>
    <div class="fact"><p class="fact-title">The Shore House isn’t theirs – it’s yours.</p><p class="fact-copy">Seabright Park is shutting down public space for 9 private Shore House raves through July. But July 5 is different — “Liberty Fest” is a full-park, alcohol-fueled rave that shuts out the public from taxpayer-owned land. These takeovers appear to violate their lease and Measure G, which protects YOUR beach for ALL — not just paying partiers.</p></div>
    <div class="fact"><p class="fact-title">Disabled child traumatized by rave noise</p><p class="fact-copy">A child with cerebral palsy and auditory sensitivity came to use the City’s Beach Accessibility Program but was overwhelmed by deafening Rave noise and fled in distress. The illegal sound levels deny All individuals with similar disabilities access to public accommodations. This is a direct violation of the Americans with Disabilities Act.</p></div>
    <div class="fact"><p class="fact-title">Exposed: is Seabright running an unethical self-dealing scheme ?</p><p class="fact-copy">Seabright Park’s General Manager, Glen Porter, is also CEO of KT Security Solutions — the very company hired by Seabright for “security” services. And who’s listed as corporate secretary? Nina Vellan, close relative of the leaseholder Marco Vellan. Is this Self-Dealing?</p></div>
    <div class="fact"><p class="fact-title">Documented runoff and suspected environmental disaster</p><p class="fact-copy">Improperly Stored Chemicals, oils, and waste water spilling into storm drains. Parking lots are trashed, flooded, and neglected. Stormwater compliance appears to be ignored.</p></div>
    <div class="fact"><p class="fact-title">Exposed: Seabright Park’s illegal signs mislead the public.</p><p class="fact-copy">They’re tricking the public into believing city-owned land is private, violating their lease which requires signage clearly stating the property is city-owned and open to all.</p></div>
    <div class="fact"><p class="fact-title">Seabright Park: accident waiting to happen?</p><p class="fact-copy">From the Grand Coaster to the rides and walkways, safety appears ignored. The lease requires independent engineer inspections — yet no reports can be found. With what looks like hundreds of code violations, the entire park may be one broken bolt from disaster. Who’s protecting the public?</p></div>
  </div>
  <div class="park-photo" role="img" aria-label="Aerial evening photo of the seaside amusement park with its wooden roller coaster, lit rides and parking lot">
    <p class="site-link">www.FixSeabrightPark.com</p>
  </div>
  <h2 class="back-rally">HELP OUR COMMUNITY SAVE SEABRIGHT PARK<br>SEABRIGHT PARK WAS BUILT FOR FAMILIES — NOT RAVES</h2>
</section>

</body>
</html>
```